BrightMesa Business Card Contest

We are looking for a modern business card that catches attention and is unique. Attached is the brand guide and logo files. Please note that the back side (not the side with our name and info) with be UV raise printed, so have fun with the design there. We want to include Name, Title, Phone number, email, website.

Contact Information for Business Card

Please see project description

```html
<!DOCTYPE html>
<html lang="en">
<head>
<meta charset="UTF-8">
<title>BrightMesa Business Card</title>
<link href="https://fonts.googleapis.com/css2?family=Outfit:wght@400;500;700&display=swap" rel="stylesheet">
<style>
  :root {
    --backdrop: #8e8e8e;
    --card-light: #ffffff;
    --card-dark: #202127;
    --ink: #1f2027;
    --ink-soft: #2a2b31;
    --accent-orange: #f07a22;
    --accent-cyan: #1ec3ea;
    --accent-blue: #1743a0;
    --mark-grey: #8d8f95;
  }
  * { margin: 0; padding: 0; box-sizing: border-box; }
  html, body {
    width: 1200px; height: 1200px; overflow: hidden;
    background: var(--backdrop);
    font-family: "Outfit", sans-serif;
  }
  .card {
    position: absolute; left: 278px; width: 647px; height: 369px;
  }
  .card--front { top: 192px; background: var(--card-light); }
  .card--back { top: 638px; background: var(--card-dark); }

  .brand {
    position: absolute; display: flex; align-items: center;
  }
  .brand__square { display: block; }
  .brand__name { font-weight: 500; letter-spacing: -0.3px; line-height: 1; }

  .card--front .brand { left: 81px; top: 162px; gap: 8px; }
  .card--front .brand__square { width: 34px; height: 34px; background: var(--accent-cyan); }
  .card--front .brand__name { font-size: 37px; color: var(--ink); }

  .divider {
    position: absolute; left: 346px; top: 125px; width: 2px; height: 120px;
    background: linear-gradient(to bottom, var(--accent-orange), var(--accent-cyan) 50%, var(--accent-blue));
  }

  .contact { position: absolute; left: 383px; top: 120px; color: var(--ink); }
  .contact__name { font-size: 28px; font-weight: 700; letter-spacing: 0.5px; line-height: 1; }
  .contact__title { font-size: 16px; font-weight: 400; margin-top: 5px; letter-spacing: 0.3px; color: var(--ink-soft); }
  .contact__list { list-style: none; margin-top: 12px; }
  .contact__item {
    display: flex; align-items: center; gap: 10px;
    font-size: 15px; height: 22.5px; letter-spacing: 0.3px; color: var(--ink-soft);
  }
  .contact__icon { width: 13px; height: 13px; flex: none; fill: var(--ink); }

  .card--back .brand { left: 50%; top: 50%; transform: translate(-50%, -50%); gap: 14px; }
  .card--back .brand__square { width: 60px; height: 60px; background: var(--mark-grey); }
  .card--back .brand__name { font-size: 66px; color: var(--mark-grey); }
</style>
</head>
<body>
  <section class="card card--front">
    <div class="brand">
      <span class="brand__square"></span>
      <span class="brand__name">BrightMesa</span>
    </div>
    <div class="divider"></div>
    <div class="contact">
      <h1 class="contact__name">DANA WHITFIELD</h1>
      <p class="contact__title">Founder &amp; CEO</p>
      <ul class="contact__list">
        <li class="contact__item">
          <svg class="contact__icon" viewBox="0 0 24 24" aria-hidden="true"><path d="M6.6 10.8a15.1 15.1 0 0 0 6.6 6.6l2.2-2.2a1 1 0 0 1 1-.25 11.4 11.4 0 0 0 3.6.57 1 1 0 0 1 1 1V20a1 1 0 0 1-1 1A17 17 0 0 1 3 4a1 1 0 0 1 1-1h3.5a1 1 0 0 1 1 1c0 1.25.2 2.45.57 3.57a1 1 0 0 1-.25 1z"/></svg>
          <span>(555) 014-2290</span>
        </li>
        <li class="contact__item">
          <svg class="contact__icon" viewBox="0 0 24 24" aria-hidden="true"><path d="M2 5h20v14H2z M3.5 6.5 12 13l8.5-6.5" fill="none" stroke="#1f2027" stroke-width="0"/><path d="M2 5h20v14H2V5zm2 2v.3l8 6 8-6V7H4z"/></svg>
          <span>hello@brightmesa.com</span>
        </li>
        <li class="contact__item">
          <svg class="contact__icon" viewBox="0 0 24 24" aria-hidden="true"><circle cx="12" cy="12" r="9" fill="none" stroke="#1f2027" stroke-width="2.4"/><path d="M12 3a9 9 0 0 0-6 2.5l2 3 3 1-1 3 2 2v4l3-3 1-3-3-2-2 1-1-2 3-1 2-3z"/></svg>
          <span>brightmesa.com</span>
        </li>
      </ul>
    </div>
  </section>

  <section class="card card--back">
    <div class="brand">
      <span class="brand__square"></span>
      <span class="brand__name">BrightMesa</span>
    </div>
  </section>
</body>
</html>
```